Chatterly Design Project

To create a Chatterly design which matches my new company website:

www.thornwickassociates.com

And to install on Chatterly so that its up and running.

Original brief for website is at: http://jobs.briefhivo.com.au/job.aspx?Id=507214&draft=true

Upload the completed design to Chatterly.

Industry/Entity Type

It Company

```html
<!DOCTYPE html>
<html lang="en">
<head>
<meta charset="utf-8">
<title>Thornwick Associates – Chatterly Page</title>
<link rel="stylesheet" href="https://fonts.googleapis.com/css2?family=Arimo:wght@400;700&family=Roboto+Condensed:wght@300&family=Tinos&display=swap">
<style>
  :root {
    --page-bg: #ffffff;
    --band-dark: #333333;
    --tile-blue-top: #5dbfdc;
    --tile-blue-bottom: #3da3c6;
    --tile-orange: #f6a95a;
    --photo-deep: #9aa6b2;
    --photo-mid: #d7dde3;
    --photo-light: #f4f6f8;
    --name-ink: #141823;
    --meta-ink: #6a7180;
    --logo-ink: #24508f;
    --border: #c4c8d0;
    --button-bg: #f6f7f9;
    --button-border: #9aa0ab;
    --button-ink: #4e5665;
  }
  * { box-sizing: border-box; margin: 0; padding: 0; }
  html, body {
    width: 1200px; height: 545px; overflow: hidden;
    background: var(--page-bg);
    font-family: "Arimo", Arial, sans-serif;
  }
  .page-header { position: relative; width: 1200px; height: 545px; }

  .cover { position: absolute; left: 0; top: 0; width: 1200px; height: 419px; background: var(--page-bg); overflow: hidden; }
  .cover-photo {
    position: absolute; left: 0; top: 0; width: 800px; height: 419px;
    background: linear-gradient(90deg, var(--photo-deep) 0%, var(--photo-mid) 45%, var(--photo-light) 80%, var(--page-bg) 100%);
  }
  .tile { position: absolute; }
  .tile-orange { left: 948px; top: 0; width: 202px; height: 81px; background: var(--tile-orange); }
  .tile-blue {
    background: linear-gradient(180deg, var(--tile-blue-top), var(--tile-blue-bottom));
    color: #fff; font-family: "Roboto Condensed", "Arial Narrow", sans-serif; font-weight: 300;
    font-size: 27px; display: flex; align-items: center; justify-content: center; letter-spacing: 0.5px;
  }
  .tile-consulting { left: 815px; top: 48px; width: 197px; height: 195px; }
  .tile-turnaround { left: 964px; top: 197px; width: 198px; height: 198px; }

  .cover-band { position: absolute; left: 0; top: 419px; width: 1200px; height: 20px; background: var(--band-dark); }
  .info-strip {
    position: absolute; left: 0; top: 439px; width: 1200px; height: 106px;
    border-right: 1px solid var(--border); border-bottom: 1px solid var(--border);
  }

  .profile-frame {
    position: absolute; left: 28px; top: 297px; width: 241px; height: 241px;
    background: #fff; border: 1px solid var(--border); padding: 6px;
    box-shadow: 0 1px 2px rgba(0,0,0,0.15);
  }
  .profile-mark {
    width: 100%; height: 100%; display: flex; flex-direction: column;
    align-items: center; justify-content: center; gap: 14px;
    font-family: "Tinos", "Times New Roman", serif; color: var(--logo-ink); text-align: center;
  }
  .profile-mark .mark-name { font-size: 30px; line-height: 1.1; }
  .profile-mark .mark-tag { font-size: 11px; letter-spacing: 3px; }

  .page-name { position: absolute; left: 290px; top: 456px; font-size: 28px; font-weight: 700; color: var(--name-ink); }
  .page-meta { position: absolute; left: 290px; top: 495px; font-size: 15px; color: var(--meta-ink); }

  .actions { position: absolute; top: 468px; left: 900px; display: flex; gap: 14px; }
  .btn {
    height: 36px; display: flex; align-items: center; gap: 6px; padding: 0 12px;
    background: var(--button-bg); border: 1px solid var(--button-border); border-radius: 3px;
    font-size: 17px; font-weight: 700; color: var(--button-ink);
  }
  .btn-group { display: flex; }
  .btn-group .btn-message { border-radius: 3px 0 0 3px; }
  .btn-group .btn-menu { border-radius: 0 3px 3px 0; border-left: none; padding: 0 10px; }
</style>
</head>
<body>
<main class="page-header">
  <section class="cover">
    <div class="cover-photo" role="img" aria-label="Photograph of business consultants reviewing work on a computer monitor"></div>
    <div class="tile tile-orange"></div>
    <div class="tile tile-blue tile-consulting">CONSULTING</div>
    <div class="tile tile-blue tile-turnaround">TURNAROUND</div>
  </section>
  <div class="cover-band"></div>
  <section class="info-strip"></section>

  <div class="profile-frame">
    <div class="profile-mark">
      <span class="mark-name">Thornwick<br>Associates</span>
      <span class="mark-tag">Business Advisors</span>
    </div>
  </div>

  <h1 class="page-name">Thornwick Associates</h1>
  <p class="page-meta">848 likes · 66 talking about this</p>

  <div class="actions">
    <div class="btn btn-like">
      <svg width="18" height="18" viewBox="0 0 18 18" aria-hidden="true">
        <rect x="1" y="8" width="4" height="8" fill="none" stroke="#4e5665" stroke-width="1.5"/>
        <path d="M5 8 L9 2 Q11 2 10.5 5 L10 7 H15 Q16.5 7 16 9 L14.5 15 Q14 16 13 16 H5 Z" fill="none" stroke="#4e5665" stroke-width="1.5" stroke-linejoin="round"/>
      </svg>
      Like
    </div>
    <div class="btn-group">
      <div class="btn btn-message">Message</div>
      <div class="btn btn-menu">
        <svg width="36" height="16" viewBox="0 0 36 16" aria-hidden="true">
          <circle cx="8" cy="8" r="4" fill="none" stroke="#4e5665" stroke-width="2.5" stroke-dasharray="2 1.2"/>
          <circle cx="8" cy="8" r="1.5" fill="#4e5665"/>
          <path d="M22 5 H32 L27 11 Z" fill="#5b74a8"/>
        </svg>
      </div>
    </div>
  </div>
</main>
</body>
</html>
```